dumoCircuit "organisation chart"

We need a new Organisation Chart for our Company! We are actually in a Change-management-process and will Change from a hierarchical Organisation in to a Network Organisation. Therefor we need a new Organisation Chart.
The following departements must be visible and legible on the Chart:
Team Sales & Consulting
Team Productmanagement
Team Supply Chain
Team Human Resources
Team Smart Digital Development
Team Marketing & Communication
The title of the Chart ist «dumoCircuit»
The Colors of the back of the Chart must be: RGB 73/25/102 // Pantone 2627
The Colors for the different Teams should be:
Team Sales & Consulting (Pantone: 803/neon yellow = Background)
Team Productmanagement (Pantone: 804/neon orange = Background)
Team Supply Chain (Pantone: 802/neon green = Background)
Team Human Resources (Pantone: 801/neon blue = Background)
Team Smart Digital Development (Pantone: 805/neon red = Background)
Team Marketing & Communication (Pantone: 803/neon pink = Background)
See below (upload files) an example showing a self-made Chart ... :-)
Our font is: Univers LT Std // Please feel free to Combine the Fonts Colors with the background colors
It Company

```html
<!DOCTYPE html>
<html lang="en">
<head>
<meta charset="utf-8">
<title>dumoCircuit – Organisation Chart</title>
<link rel="stylesheet" href="https://fonts.googleapis.com/css2?family=Archivo:wght@600;700;800&display=swap">
<style>
  :root {
    --backdrop: #491966;
    --ink: #ffffff;
    --team-sales: #e3f04f;
    --team-sales-ink: #e9275a;
    --team-product: #ff8000;
    --team-supply: #6fcf0a;
    --team-hr: #3388ff;
    --team-digital: #ec2c52;
    --team-marketing: #e80aa9;
  }
  html, body {
    margin: 0;
    padding: 0;
    overflow: hidden;
    background: var(--backdrop);
  }
  .chart {
    position: relative;
    width: 873px;
    height: 1200px;
    background: var(--backdrop);
    font-family: "Archivo", Arial, sans-serif;
    overflow: hidden;
  }
  .chart-title {
    position: absolute;
    left: 0;
    right: 0;
    top: 142px;
    margin: 0;
    text-align: center;
    font-size: 52px;
    font-weight: 600;
    letter-spacing: 1px;
    color: var(--ink);
    line-height: 1;
  }
  .network { position: absolute; inset: 0; }
  .link { stroke: var(--ink); stroke-width: 3.5; fill: none; }
  .arrow-head { stroke: var(--ink); stroke-width: 1.6; fill: none; stroke-linecap: round; stroke-linejoin: round; }
  .hex { stroke-width: 18; stroke-linejoin: round; }
  .team-label { font-family: "Archivo", Arial, sans-serif; text-anchor: middle; fill: var(--ink); }
  .team-word { font-size: 27px; font-weight: 700; }
  .team-name { font-size: 14px; font-weight: 700; letter-spacing: 0.3px; }
  .team-name--compact { font-size: 12.5px; }
  .team--sales .hex { fill: var(--team-sales); stroke: var(--team-sales); }
  .team--sales .team-label { fill: var(--team-sales-ink); }
  .team--product .hex { fill: var(--team-product); stroke: var(--team-product); }
  .team--supply .hex { fill: var(--team-supply); stroke: var(--team-supply); }
  .team--hr .hex { fill: var(--team-hr); stroke: var(--team-hr); }
  .team--digital .hex { fill: var(--team-digital); stroke: var(--team-digital); }
  .team--marketing .hex { fill: var(--team-marketing); stroke: var(--team-marketing); }
</style>
</head>
<body>
<main class="chart">
  <h1 class="chart-title">dumoCircuit</h1>

  <svg class="network" viewBox="0 0 873 1200" width="873" height="1200" aria-label="Network organisation chart of six teams">
    <defs>
      <marker id="arrow-head" viewBox="0 0 12 12" refX="10" refY="6" markerWidth="5" markerHeight="5" orient="auto-start-reverse">
        <path class="arrow-head" d="M2 1 L10 6 L2 11"/>
      </marker>
      <polygon id="hex-shape" points="0,-76 65,-38 65,38 0,76 -65,38 -65,-38"/>
    </defs>

    <g class="links">
      <line class="link" x1="383" y1="419" x2="468" y2="419" marker-start="url(#arrow-head)" marker-end="url(#arrow-head)"/>
      <line class="link" x1="623" y1="504" x2="670" y2="574" marker-start="url(#arrow-head)" marker-end="url(#arrow-head)"/>
      <line class="link" x1="663" y1="750" x2="617" y2="821" marker-start="url(#arrow-head)" marker-end="url(#arrow-head)"/>
      <line class="link" x1="470" y1="907" x2="385" y2="907" marker-start="url(#arrow-head)" marker-end="url(#arrow-head)"/>
      <line class="link" x1="238" y1="824" x2="191" y2="752" marker-start="url(#arrow-head)" marker-end="url(#arrow-head)"/>
      <line class="link" x1="189" y1="571" x2="237" y2="499" marker-start="url(#arrow-head)" marker-end="url(#arrow-head)"/>
      <line class="link" x1="248" y1="665" x2="626" y2="665" marker-start="url(#arrow-head)" marker-end="url(#arrow-head)"/>
      <line class="link" x1="330" y1="502" x2="545" y2="822" marker-start="url(#arrow-head)" marker-end="url(#arrow-head)"/>
      <line class="link" x1="545" y1="506" x2="330" y2="826" marker-start="url(#arrow-head)" marker-end="url(#arrow-head)"/>
    </g>

    <g class="team team--sales" transform="translate(299 424)">
      <use href="#hex-shape" class="hex"/>
      <text class="team-label team-word" y="-14">TEAM</text>
      <text class="team-label team-name" y="8">SALES</text>
      <text class="team-label team-name" y="21">&amp;</text>
      <text class="team-label team-name" y="34">CONSULTING</text>
    </g>

    <g class="team team--product" transform="translate(573 422)">
      <use href="#hex-shape" class="hex"/>
      <text class="team-label team-word" y="-14">TEAM</text>
      <text class="team-label team-name" y="9">PRODUCT</text>
      <text class="team-label team-name" y="25">MANAGEMENT</text>
    </g>

    <g class="team team--marketing" transform="translate(155 658)">
      <use href="#hex-shape" class="hex"/>
      <text class="team-label team-word" y="-14">TEAM</text>
      <text class="team-label team-name team-name--compact" y="6">MARKETING</text>
      <text class="team-label team-name team-name--compact" y="19">&amp;</text>
      <text class="team-label team-name team-name--compact" y="32">COMMUNICATION</text>
    </g>

    <g class="team team--supply" transform="translate(708 658)">
      <use href="#hex-shape" class="hex"/>
      <text class="team-label team-word" y="-14">TEAM</text>
      <text class="team-label team-name" y="12">SUPPLY</text>
      <text class="team-label team-name" y="28">CHAIN</text>
    </g>

    <g class="team team--digital" transform="translate(299 905)">
      <use href="#hex-shape" class="hex"/>
      <text class="team-label team-word" y="-19">TEAM</text>
      <text class="team-label team-name" y="3">SMART</text>
      <text class="team-label team-name" y="19">DIGITAL</text>
      <text class="team-label team-name" y="35">DEVELOPMENT</text>
    </g>

    <g class="team team--hr" transform="translate(588 903)">
      <use href="#hex-shape" class="hex"/>
      <text class="team-label team-word" y="-18">TEAM</text>
      <text class="team-label team-name" y="9">HUMAN</text>
      <text class="team-label team-name" y="25">RESOURCES</text>
    </g>
  </svg>
</main>
</body>
</html>
```